Quorvex business card design

create modern and tech looking business card that is clean but effectively communciates that we are a cloud communications company.
Should have at minimum:
Employee Name
Postion
Phone Number
Email
website
create modern and tech looking business card that is clean but effectively communciates that we are a cloud communications company. We have two logo color schemes (attached) so would like to see designs both ways
Should have at minimum:
Employee Name
Postion
Phone Number
Email
website

```html
<!DOCTYPE html>
<html lang="en">
<head>
<meta charset="utf-8">
<title>Quorvex business card</title>
<link href="https://fonts.googleapis.com/css2?family=Questrial&display=swap" rel="stylesheet">
<style>
  :root {
    --stage: #2b2b2d;
    --card: #f4f4f4;
    --card-shade: #e6e6e6;
    --ink: #4a4a4c;
    --ink-soft: #5c5c5e;
    --lime: #8cc63f;
    --cyan: #2ec4dc;
    --ocean: #1a8fc0;
  }
  * { margin: 0; padding: 0; box-sizing: border-box; }
  html, body { width: 1200px; height: 834px; overflow: hidden; }
  body {
    background: var(--stage);
    font-family: "Questrial", sans-serif;
    color: var(--ink);
    position: relative;
  }
  .card {
    position: absolute;
    width: 500px;
    height: 286px;
    background: linear-gradient(135deg, #fafafa 0%, var(--card) 55%, var(--card-shade) 100%);
    box-shadow: 0 14px 30px rgba(0,0,0,.45);
    overflow: hidden;
  }
  .card--front { left: 90px; top: 100px; }
  .card--back { left: 610px; top: 448px; }

  .brand {
    position: absolute;
    left: 130px;
    top: 124px;
    display: flex;
    align-items: center;
    gap: 10px;
  }
  .brand__dot {
    width: 22px; height: 22px;
    border-radius: 50%;
    background: var(--cyan);
  }
  .brand__name {
    font-size: 26px;
    letter-spacing: 2px;
    color: var(--ink);
    text-transform: uppercase;
  }

  .band { position: absolute; }
  .band--top {
    right: 0; top: 0;
    width: 300px; height: 14px;
    background: var(--cyan);
    border-bottom-left-radius: 12px;
  }
  .band--bottom {
    right: 0; bottom: 0;
    width: 190px; height: 34px;
    background: linear-gradient(90deg, var(--ocean), var(--cyan));
    border-top-left-radius: 18px;
  }

  .person {
    position: absolute;
    left: 60px;
    top: 142px;
  }
  .person__name { font-size: 24px; color: var(--ink); font-weight: 400; letter-spacing: .3px; }
  .person__role { font-size: 16px; color: var(--lime); margin-top: 2px; margin-left: 34px; }

  .contact {
    position: absolute;
    left: 262px;
    top: 96px;
    list-style: none;
  }
  .contact__item {
    display: flex;
    align-items: center;
    gap: 12px;
    font-size: 13px;
    color: var(--ink-soft);
    margin-bottom: 9px;
  }
  .contact__icon { width: 16px; height: 16px; flex: none; }
</style>
</head>
<body>

<section class="card card--front" aria-label="Card front">
  <div class="brand">
    <span class="brand__dot"></span>
    <span class="brand__name">Quorvex</span>
  </div>
</section>

<section class="card card--back" aria-label="Card back">
  <span class="band band--top"></span>
  <span class="band band--bottom"></span>

  <div class="person">
    <p class="person__name">Dara Lindqvist</p>
    <p class="person__role">President</p>
  </div>

  <ul class="contact">
    <li class="contact__item">
      <svg class="contact__icon" viewBox="0 0 16 16" fill="none" stroke="#2ec4dc" stroke-width="1.3">
        <path d="M4 2l2 3-1.5 1.5a8 8 0 0 0 5 5L11 10l3 2-1.5 2.5C7 14 2 9 1.5 3.5z"/>
      </svg>
      <span>4815 162 342</span>
    </li>
    <li class="contact__item">
      <svg class="contact__icon" viewBox="0 0 16 16" fill="none" stroke="#2ec4dc" stroke-width="1.3">
        <rect x="1.5" y="3.5" width="13" height="9"/><path d="M1.5 3.5l6.5 5 6.5-5"/>
      </svg>
      <span>hello@quorvex.com</span>
    </li>
    <li class="contact__item">
      <svg class="contact__icon" viewBox="0 0 16 16" fill="none" stroke="#2ec4dc" stroke-width="1.3">
        <circle cx="8" cy="8" r="6.5"/><ellipse cx="8" cy="8" rx="3" ry="6.5"/><path d="M1.5 8h13"/>
      </svg>
      <span>www.quorvex.com</span>
    </li>
  </ul>
</section>

</body>
</html>
```